TKR Advisory Business Cards

Hi there,

I'd like to make a simple new business card design with the logo we already have created for our business.

I need a double sided business card with our logo on the front side and the company and person's details on the back side.

I'd like it to be on a white background and no background so I can potentially use it with either white paper or put it on different coloured paper in accordance with our business colours.

Please use the logo images I have attached and also the fonts.

So Front side:
- Logo in centre of business card (use medium logo so there is a pretty decent border around it, so don't want to fill the whole card but to make it prominent).

Back Side.
- We need 3 different business cards with the different people's name on each.

ie.

Dorian Halvreck
Business Development Manager

m +61 437 206 518
e dorian@tkradvisory.com.au
w tkradvisory.com.au

- Also I'd like to put only the cog/power button logo in the top right hand corner of the card.
(You might need to chop the current logo in half as I don't have a seperate log just for this)
- Also I'd like some lines running on the top left hand corner diagonally, anything that will add to the design or some swirling lines that add some cool effect to the card.

Also I'd like to maybe put our ABN in the bottom right hand corner of the card in a smaller font.

I'd like to also talk to the designer if possible so I can get my idea across a bit better.

Thanks!

Regards,
Dorian

```html
<!DOCTYPE html>
<html lang="en">
<head>
<meta charset="utf-8">
<title>TKR Advisory Business Cards</title>
<link rel="stylesheet" href="https://fonts.googleapis.com/css2?family=Lato:wght@400;700&display=swap">
<style>
  :root {
    --page-bg: #e6e6e6;
    --card-black: #0b0b0b;
    --card-white: #ffffff;
    --orange: #f7a21b;
    --orange-deep: #f28c10;
    --orange-light: #fbc04a;
    --charcoal: #4a4a4a;
    --ink: #1a1a1a;
  }
  * { box-sizing: border-box; margin: 0; padding: 0; }
  html, body {
    width: 1200px;
    height: 926px;
    overflow: hidden;
    background: var(--page-bg);
    font-family: "Lato", sans-serif;
  }
  .sheet {
    width: 1200px;
    height: 926px;
    display: flex;
    flex-direction: column;
    align-items: center;
    justify-content: center;
    gap: 40px;
  }
  .card {
    position: relative;
    width: 680px;
    height: 416px;
    overflow: hidden;
    box-shadow: 0 6px 18px rgba(0,0,0,0.18);
  }

  /* Front side */
  .card--front {
    background: var(--card-black);
    display: flex;
    align-items: center;
    justify-content: center;
  }
  .brand {
    display: flex;
    align-items: center;
    gap: 14px;
  }
  .brand__dot {
    width: 46px;
    height: 46px;
    border-radius: 50%;
    background: var(--orange);
  }
  .brand__name {
    font-weight: 700;
    color: var(--orange);
    font-size: 50px;
    letter-spacing: -0.5px;
  }

  /* Back side */
  .card--back { background: var(--card-white); }
  .card--back .brand {
    position: absolute;
    top: 40px;
    left: 38px;
    gap: 10px;
  }
  .card--back .brand__dot { width: 30px; height: 30px; }
  .card--back .brand__name { font-size: 32px; }

  .person {
    position: absolute;
    top: 108px;
    right: 36px;
    text-align: right;
    color: var(--ink);
  }
  .person__name { font-size: 27px; font-weight: 400; }
  .person__role { font-size: 15px; margin-top: 4px; }

  .contact {
    position: absolute;
    top: 150px;
    left: 38px;
    list-style: none;
    color: var(--ink);
    font-size: 17px;
    line-height: 1.35;
  }
  .contact__label { font-weight: 700; margin-right: 4px; }

  .swoosh {
    position: absolute;
    inset: 0;
    width: 680px;
    height: 416px;
  }
</style>
</head>
<body>
<main class="sheet">
  <section class="card card--front" aria-label="Card front">
    <div class="brand">
      <span class="brand__dot"></span>
      <span class="brand__name">TKR Advisory</span>
    </div>
  </section>

  <section class="card card--back" aria-label="Card back">
    <svg class="swoosh" viewBox="0 0 680 416" aria-hidden="true">
      <defs>
        <linearGradient id="band" x1="0" y1="0" x2="1" y2="0">
          <stop offset="0" stop-color="var(--orange-deep)"/>
          <stop offset="0.6" stop-color="var(--orange)"/>
          <stop offset="1" stop-color="var(--orange-light)"/>
        </linearGradient>
      </defs>
      <path d="M0 232 C 160 236, 330 268, 470 320 C 560 352, 630 380, 680 396 L680 416 L0 416 Z" fill="url(#band)"/>
      <path d="M0 262 C 170 262, 330 290, 500 352" fill="none" stroke="#ffffff" stroke-width="10" stroke-linecap="round" opacity="0.95"/>
      <path d="M0 250 C 160 248, 300 268, 440 310" fill="none" stroke="#ffffff" stroke-width="2" opacity="0.6"/>
      <path d="M0 245 C 140 242, 260 256, 380 282" fill="none" stroke="var(--orange-light)" stroke-width="3" opacity="0.8"/>
      <circle cx="596" cy="372" r="150" fill="var(--charcoal)"/>
    </svg>

    <div class="brand">
      <span class="brand__dot"></span>
      <span class="brand__name">TKR Advisory</span>
    </div>

    <div class="person">
      <p class="person__name">Dorian Halvreck</p>
      <p class="person__role">Business Development Manager</p>
    </div>

    <ul class="contact">
      <li><span class="contact__label">m :</span>+61 437 206 518</li>
      <li><span class="contact__label">e :</span>dorian@tkradvisory.com.au</li>
      <li><span class="contact__label">w :</span>tkradvisory.com.au</li>
    </ul>
  </section>
</main>
</body>
</html>
```